Silver Bloom Marisol's Cleaning Service Business Cards Project

A business card with all contact details with logo design on there (already have a logo) eye catching Logo and contact info on one side, full logo on the back, must target upper class residential and corporate companies, fitness companies, still keep it on the feminine side of things , must look elegant

Target Market(s)

Upper class homes and corporate companies

Industry/Entity Type

Cleaning Service

Contact Information for Business Card

Name: Marisol Venturo
Position: Director
ABN: 47193802564
Email: marisolssilvercleaning@fernmail.test
Number: 0417968341

Font styles to use
Decorative

Colors

Designer to choose colors to be used in the design.

Requirements
Must have
• Available Sydney Wide, contact info and logo on one side, full logo on the back
Nice to have
• Professional appearance
Should not have
• Cheap advert looking stuff

```html
<!DOCTYPE html>
<html lang="en">
<head>
<meta charset="utf-8">
<title>Silver Bloom – Business Cards</title>
<link href="https://fonts.googleapis.com/css2?family=Cinzel:wght@500&family=Roboto:wght@400;500&family=Roboto+Condensed:wght@500;700&display=swap" rel="stylesheet">
<style>
  :root {
    --stage: #e9e6e1;
    --card-front: #1b1c1e;
    --card-back: #2d3240;
    --teal: #2fe6dd;
    --teal-pale: #aef7f6;
    --white: #ffffff;
    --ink: #0e0f10;
  }
  * { margin: 0; padding: 0; box-sizing: border-box; }
  html, body { width: 1200px; height: 960px; overflow: hidden; }
  body {
    background: var(--stage);
    position: relative;
    font-family: "Roboto", Arial, sans-serif;
    color: var(--white);
  }
  .card {
    position: absolute;
    width: 601px;
    height: 343px;
    box-shadow: 0 4px 10px rgba(0,0,0,0.25);
  }
  .card--front { left: 314px; top: 113px; background: var(--card-front); }
  .card--back  { left: 311px; top: 472px; background: var(--card-back); }

  /* Front: name plate */
  .name-plate__shadow {
    position: absolute; left: 19px; top: 157px;
    width: 238px; height: 52px; background: var(--teal-pale);
  }
  .name-plate {
    position: absolute; left: 0; top: 170px;
    width: 240px; height: 54px; background: var(--teal);
    border: 2px solid var(--ink);
    padding: 6px 0 0 35px;
  }
  .name-plate__name {
    font-family: "Roboto Condensed", Arial, sans-serif;
    font-weight: 700; font-size: 20px; line-height: 22px;
    color: var(--white); text-transform: uppercase;
  }
  .name-plate__role {
    font-family: "Roboto Condensed", Arial, sans-serif;
    font-weight: 500; font-size: 15px; line-height: 17px;
    color: var(--white); text-transform: uppercase;
  }

  /* Front: contact list */
  .contact-list {
    position: absolute; left: 35px; top: 257px;
    list-style: none;
  }
  .contact-list__item {
    display: flex; align-items: center;
    font-size: 14px; line-height: 19px; height: 19px;
  }
  .contact-list__icon { width: 13px; height: 13px; margin-right: 9px; fill: var(--teal); }
  .abn {
    position: absolute; right: 39px; top: 292px;
    font-size: 14px;
  }

  /* Brand wordmark */
  .brand { position: absolute; text-align: center; }
  .brand--front { left: 343px; top: 144px; width: 240px; }
  .brand__name {
    font-family: "Cinzel", Georgia, serif;
    font-weight: 500; color: var(--teal);
    text-transform: uppercase; letter-spacing: 1px;
  }
  .brand--front .brand__name { font-size: 21px; line-height: 24px; }
  .brand__tagline {
    font-size: 8px; letter-spacing: 2px; text-transform: uppercase;
    color: var(--white); margin-top: 3px;
  }
  .brand__area {
    font-family: "Cinzel", Georgia, serif;
    font-size: 10px; letter-spacing: 2px;
    color: var(--teal); margin-top: 10px;
  }
  .brand--back { left: 0; width: 601px; top: 138px; }
  .brand--back .brand__name { font-size: 38px; line-height: 44px; letter-spacing: 3px; }

  .website-line {
    position: absolute; left: 0; width: 601px; top: 289px;
    text-align: center; font-size: 14px; letter-spacing: 4px;
  }
</style>
</head>
<body>

<section class="card card--front" aria-label="Business card front">
  <div class="name-plate__shadow"></div>
  <div class="name-plate">
    <div class="name-plate__name">Marisol Venturo</div>
    <div class="name-plate__role">Director</div>
  </div>

  <ul class="contact-list">
    <li class="contact-list__item">
      <svg class="contact-list__icon" viewBox="0 0 24 24"><path d="M6.6 10.8a15.1 15.1 0 0 0 6.6 6.6l2.2-2.2a1 1 0 0 1 1-.25 11.4 11.4 0 0 0 3.6.57 1 1 0 0 1 1 1V20a1 1 0 0 1-1 1A17 17 0 0 1 3 4a1 1 0 0 1 1-1h3.5a1 1 0 0 1 1 1c0 1.25.2 2.45.57 3.57a1 1 0 0 1-.25 1z"/></svg>
      0417968341
    </li>
    <li class="contact-list__item">
      <svg class="contact-list__icon" viewBox="0 0 24 24"><path d="M2 5h20v14H2z"/><path d="M2 6l10 7 10-7" fill="none" stroke="#1b1c1e" stroke-width="1.8"/></svg>
      marisolssilvercleaning@fernmail.test
    </li>
    <li class="contact-list__item">
      <svg class="contact-list__icon" viewBox="0 0 24 24"><circle cx="12" cy="12" r="10"/><path d="M2 12h20M12 2c3 3 3 17 0 20M12 2c-3 3-3 17 0 20" fill="none" stroke="#1b1c1e" stroke-width="1.6"/></svg>
      www.silverbloom.test
    </li>
  </ul>

  <div class="abn">ABN: 47193802564</div>

  <div class="brand brand--front">
    <div class="brand__name">Silver Bloom</div>
    <div class="brand__tagline">Marisol's Cleaning Services</div>
    <div class="brand__area">Available Sydney Wide</div>
  </div>
</section>

<section class="card card--back" aria-label="Business card back">
  <div class="brand brand--back">
    <div class="brand__name">Silver Bloom</div>
  </div>
  <div class="website-line">www.silverbloom.test</div>
</section>

</body>
</html>
```